Mirvald Health & Wellness needs a fresh and interesting website

I need a rebrand and redevelopment of my website, www.tessapinlowe.com
Our mission is provide bespoke , lifestyle medicine , everyone has their own path to health. and we are creating a personalized experience for people to life their life to the fullest
Mirvald - means sea lands
I need an landing page and about page and potentially a few project launch pages , I have been using Wordpress for my basic information and then I use Kartra for the launch pages of my programs since I can edit those easily.

Target Market(s)

Corporate and individual's who are interested in a different perspective on health and wellness , and living with a chronic illness

Industry/Entity Type

Health, lifestyle , wellness coaching and medicine

Coding

Number of Pages Required

2 page

Font styles to use
Other font styles liked:
• look into the logo

Requirements
Must have
• the logo I uploaded
Nice to have
• I want a fresh perspective on health, I have bamboo, hibiscus vibes in my logo , but also like more of a water vibe/ I want something earthy but not too boho it needs to be clean
Should not have
• every other holistic health vibe,

```html
<!DOCTYPE html>
<html lang="en">
<head>
<meta charset="utf-8">
<title>Mirvald Health &amp; Wellness</title>
<link href="https://fonts.googleapis.com/css2?family=Playfair+Display:wght@400;500;600&family=Poppins:wght@400;500;600;700&display=swap" rel="stylesheet">
<style>
:root{
  --navy:#1c5e88;
  --heading:#1f6391;
  --cyan:#1fa8d8;
  --green:#78b800;
  --green-dark:#6aa617;
  --mist:#e5eeec;
  --text:#4a4a4a;
  --white:#ffffff;
  --footer:#195a80;
}
*{box-sizing:border-box;margin:0;padding:0}
html,body{width:1200px;height:4199px;overflow:hidden;background:var(--white)}
body{font-family:"Poppins",sans-serif;color:var(--text)}
.page{position:relative;width:1200px;height:4199px;overflow:hidden}
.abs{position:absolute}
.serif{font-family:"Playfair Display",serif}
.btn{position:absolute;display:flex;align-items:center;justify-content:center;border-radius:26px;color:var(--white);font-weight:700;font-size:14px;letter-spacing:.2px;text-transform:uppercase}
.btn-cyan{background:var(--cyan)}
.btn-green{background:var(--green)}
.photo{position:absolute}

/* header */
.site-header{position:absolute;left:0;top:0;width:1200px;height:123px;background:var(--white)}
.brand{position:absolute;left:128px;top:44px;font-family:"Poppins",sans-serif;font-weight:600;font-size:34px;color:var(--heading);display:flex;align-items:center;gap:10px}
.brand .dot{width:22px;height:22px;border-radius:50%;background:var(--cyan)}
.header-phone{position:absolute;right:128px;top:28px;display:flex;align-items:center;gap:8px;color:var(--green-dark);font-weight:600;font-size:21px}
.main-nav{position:absolute;right:128px;top:79px;display:flex;gap:38px;font-size:16px;font-weight:500;color:#222}
.main-nav .active{color:var(--green-dark)}

/* hero */
.hero-photo{left:0;top:123px;width:1200px;height:740px;background:linear-gradient(120deg,#6e8a4c 0%,#a2876f 30%,#9a8f7e 55%,#7c8f66 80%,#b6ae8d 100%)}
.hero-title{left:700px;top:290px;color:var(--white);text-shadow:0 2px 10px rgba(0,0,0,.25)}
.hero-title .name{font-family:"Playfair Display",serif;font-size:84px;line-height:1;font-weight:500;letter-spacing:1px}
.hero-title .tag{font-family:"Poppins",sans-serif;font-weight:700;font-size:38px;line-height:1.3}

/* mission */
.section-title{font-family:"Playfair Display",serif;font-weight:500;color:var(--heading);font-size:42px;line-height:1.15}
.body-copy{font-size:15px;line-height:21px;color:var(--text)}
.mission-title{left:0;width:1200px;top:920px;text-align:center}
.mission-copy{left:205px;width:790px;top:985px;text-align:center}

/* about */
.about-photo{left:-30px;top:1278px;width:545px;height:540px;border-radius:50%;background:radial-gradient(circle at 60% 40%,#d9cfc3,#9c8f7f 55%,#e07a48 85%)}
.about-title{left:600px;top:1342px}
.about-copy{left:600px;top:1458px;width:370px;font-size:15px;line-height:21px}
.hibiscus{left:985px;top:1550px;width:215px;height:290px;border-radius:45% 0 0 50%;background:radial-gradient(circle at 45% 40%,#e5262a,#c2161b 55%,#4d7c2e 90%)}

/* programs */
.programs-title{left:127px;top:2070px}
.programs-copy{left:127px;top:2145px;width:475px}
.programs-photo{left:695px;top:1960px;width:520px;height:530px;border-radius:50%;background:linear-gradient(160deg,#c8d8b8,#7f9c62 50%,#4e6b3a);border:16px solid var(--white);box-shadow:0 0 0 1px #dfe7e4}

/* services */
.services-title{left:0;width:1200px;top:2618px;text-align:center;color:var(--white)}
.core-ring{left:460px;top:2714px;width:280px;height:280px;border-radius:50%;background:#a6d35c}
.core{left:482px;top:2736px;width:236px;height:236px;border-radius:50%;background:var(--white);display:flex;align-items:center;justify-content:center;font-weight:600;font-size:30px;color:var(--heading)}
.svc-icon{width:92px;height:92px;border-radius:50%;background:var(--cyan);border:3px solid #bfe6f4;display:flex;align-items:center;justify-content:center}
.svc{width:250px;color:var(--white)}
.svc h3{font-size:17px;font-weight:600;margin-bottom:6px}
.svc p{font-size:14px;line-height:21px}
.svc.left{text-align:right}

/* follow */
.follow-title{left:0;width:1200px;top:3222px;text-align:center}
.feed-photo{top:3315px;width:187px;height:233px}

/* footer */
.footer-brand{left:132px;top:3975px;color:var(--white);font-weight:500;font-size:52px;display:flex;align-items:center;gap:14px}
.footer-brand .dot{width:30px;height:30px;border-radius:50%;background:var(--white)}
.footer-col{top:3880px;color:var(--white)}
.footer-col h4{font-family:"Playfair Display",serif;font-weight:600;font-size:24px;margin-bottom:10px}
.footer-col li{list-style:none;font-size:15px;line-height:30px}
.social{top:3933px;width:40px;height:40px;border-radius:50%;border:2px solid var(--white)}
.copyright{left:0;width:1200px;top:4114px;text-align:center;color:var(--white);font-size:15px}
</style>
</head>
<body>
<div class="page">

  <!-- header -->
  <header class="site-header">
    <div class="brand"><span class="dot"></span>Mirvald</div>
    <div class="header-phone">
      <svg width="24" height="24" viewBox="0 0 24 24" fill="none" stroke="#6aa617" stroke-width="2" stroke-linecap="round" stroke-linejoin="round"><path d="M22 16.9v3a2 2 0 0 1-2.2 2 19.8 19.8 0 0 1-8.6-3.1 19.5 19.5 0 0 1-6-6A19.8 19.8 0 0 1 2.1 4.2 2 2 0 0 1 4.1 2h3a2 2 0 0 1 2 1.7c.1 1 .4 1.9.7 2.8a2 2 0 0 1-.5 2.1L8 9.9a16 16 0 0 0 6 6l1.3-1.3a2 2 0 0 1 2.1-.4c.9.3 1.8.6 2.8.7a2 2 0 0 1 1.7 2z"/></svg>
      Call: 00X 552610
    </div>
    <nav class="main-nav">
      <span class="active">Home</span><span>About</span><span>Services</span><span>Fall Mini Retreat</span><span>Programs</span><span>Contact</span>
    </nav>
  </header>

  <!-- hero -->
  <div class="photo hero-photo" role="img" aria-label="Portrait of the practitioner seated outdoors in a red hat and wrap, garden greenery behind"></div>
  <div class="abs hero-title">
    <div class="name">MIRVALD</div>
    <div class="tag">HEALTH &amp; WELLNESS</div>
  </div>
  <div class="btn btn-cyan" style="left:700px;top:447px;width:200px;height:50px">Request a quote</div>

  <svg class="abs" style="left:0;top:640px" width="1200" height="520" viewBox="0 0 1200 520">
    <path d="M0 60 C250 20 420 40 620 120 C820 200 1000 210 1200 110 L1200 520 L0 520 Z" fill="#e5eeec"/>
    <path d="M0 60 C250 20 420 40 620 120 C820 200 1000 210 1200 110 L1200 145 C1000 240 800 225 610 140 C420 60 250 45 0 70 Z" fill="#1c5e88"/>
  </svg>

  <!-- mission -->
  <h2 class="abs section-title mission-title">Our Mission</h2>
  <p class="abs body-copy mission-copy">Lorem ipsum dolor sit amet, consectetur adipiscing elit, sed do eiusmod tempor incididunt ut labore et dolore magna aliqua. Quis ipsum suspendisse ultrices gravidaisus Lorem ipsum dolor sit amet, consectetur adipiscing elit, sed do eiusmod tempor incididunt ut labore et dolore magna aliqua. Quis ipsum suspendisse ultrices gravidaisus commodo viverracommodo viverra</p>

  <svg class="abs" style="left:0;top:1100px" width="1200" height="140" viewBox="0 0 1200 140">
    <path d="M0 0 L1200 0 L1200 60 C900 60 400 60 0 25 Z" fill="#e5eeec"/>
    <path d="M0 30 C300 70 600 85 920 82 C600 95 300 95 0 60 Z" fill="#78b800"/>
    <path d="M230 97 C550 108 900 95 1200 60 L1200 95 C900 125 550 125 230 97 Z" fill="#1fa8d8"/>
  </svg>

  <!-- about -->
  <div class="photo about-photo" role="img" aria-label="The practitioner smiling on a porch chair holding a mug"></div>
  <h2 class="abs section-title about-title">Dr Tessa P Pinlowe<br>DACM, L.Ac.</h2>
  <p class="abs body-copy about-copy">At a young age, I discovered the transformative power of Eastern Medicine when it helped me overcome lung concerns, propelling me toward my dreams as a young athlete. Years later, I faced a pivotal choice: How could I best serve and heal my community? The answer was crystal clear—Eastern Medicine.</p>
  <div class="btn btn-cyan" style="left:600px;top:1635px;width:148px;height:50px">Read more</div>
  <div class="photo hibiscus" role="img" aria-label="Red hibiscus flower with leaves"></div>

  <!-- programs -->
  <svg class="abs" style="left:0;top:1780px" width="1200" height="760" viewBox="0 0 1200 760">
    <path d="M0 240 C250 110 500 20 800 10 C950 5 1100 15 1200 30 L1200 650 C900 680 500 720 0 660 Z" fill="#e5eeec"/>
  </svg>
  <h2 class="abs section-title programs-title">Our Programs</h2>
  <p class="abs body-copy programs-copy">Lorem ipsum dolor sit amet, consectetur adipiscing elit, sed do eiusmod tempor incididunt ut labore et dolore magna aliqua. Quis ipsum suspendisse ultrices gravidaisus commodo viverraLorem ipsum dolor sit amet, consectetur adipiscing elit, sed do eiusmod tempor incididunt ut labore et dolore mag na aliqua. Quis ipsum suspendisse ultrices gravidaisus commodo viverra</p>
  <div class="btn btn-green" style="left:128px;top:2313px;width:149px;height:49px">Read more</div>
  <div class="photo programs-photo" role="img" aria-label="Woman in a green top gazing up through a bamboo forest"></div>

  <!-- services -->
  <svg class="abs" style="left:0;top:2420px" width="1200" height="760" viewBox="0 0 1200 760">
    <path d="M0 110 C400 110 800 60 1200 0 L1200 760 L0 760 Z" fill="#78b800"/>
    <path d="M0 20 C200 75 420 80 670 30 C420 95 200 110 0 90 Z" fill="#1fa8d8"/>
  </svg>
  <h2 class="abs section-title services-title">Services</h2>
  <div class="abs core-ring"></div>
  <div class="abs core">Mirvald</div>

  <div class="abs svc left" style="left:82px;top:2732px"><h3>Bespoke</h3><p>Lorem ipsum dolor sam consectetur adipiscing eli sed do eiusmod temo.</p></div>
  <div class="abs svc-icon" style="left:347px;top:2738px">
    <svg width="46" height="46" viewBox="0 0 46 46" fill="none" stroke="#fff" stroke-width="2"><rect x="6" y="5" width="20" height="12" rx="4"/><rect x="22" y="11" width="18" height="10" rx="4"/><circle cx="14" cy="29" r="4"/><circle cx="32" cy="29" r="4"/><path d="M7 41c0-5 3-7 7-7s7 2 7 7M25 41c0-5 3-7 7-7s7 2 7 7"/></svg>
  </div>
  <div class="abs svc left" style="left:82px;top:2877px"><h3>Lifestyle Medicine</h3><p>Lorem ipsum dolor sam consectetur adipiscing eli sed do eiusmod temo.</p></div>
  <div class="abs svc-icon" style="left:347px;top:2882px">
    <svg width="46" height="46" viewBox="0 0 46 46" fill="none" stroke="#fff" stroke-width="2"><path d="M6 22h34c0 9-7 15-17 15S6 31 6 22z"/><path d="M16 37l-1 4h16l-1-4"/><path d="M24 20l10-12"/><circle cx="15" cy="14" r="4"/></svg>
  </div>
  <div class="abs svc-icon" style="left:753px;top:2738px">
    <svg width="46" height="46" viewBox="0 0 46 46" fill="none" stroke="#fff" stroke-width="2"><path d="M14 40v-7c-4-3-6-7-6-12 0-8 7-14 15-14s15 6 15 14c0 3-1 5-2 7l2 5h-4v5h-6v2"/><circle cx="23" cy="20" r="6"/></svg>
  </div>
  <div class="abs svc" style="left:862px;top:2732px"><h3>Health</h3><p>Lorem ipsum dolor sam consectetur adipiscing eli sed do eiusmod temo.</p></div>
  <div class="abs svc-icon" style="left:753px;top:2882px">
    <svg width="46" height="46" viewBox="0 0 46 46" fill="none" stroke="#fff" stroke-width="2"><circle cx="23" cy="23" r="17"/><path d="M23 14c-4 4-4 10 0 14 4-4 4-10 0-14zM14 22c2 5 5 7 9 7M32 22c-2 5-5 7-9 7M23 29v8"/></svg>
  </div>
  <div class="abs svc" style="left:862px;top:2877px"><h3>wellness coaching</h3><p>Lorem ipsum dolor sam consectetur adipiscing eli sed do eiusmod temo.</p></div>

  <!-- follow -->
  <h2 class="abs section-title follow-title">@Folow Us</h2>
  <div class="photo feed-photo" style="left:98px;background:linear-gradient(160deg,#d9c9b3,#8d735c)" role="img" aria-label="Two friends taking a selfie indoors"></div>
  <div class="photo feed-photo" style="left:302px;background:linear-gradient(160deg,#b9a87c,#5c5a3e)" role="img" aria-label="Group selfie outdoors in autumn"></div>
  <div class="photo feed-photo" style="left:506px;background:linear-gradient(180deg,#8aa2b8,#5b6c6a 55%,#3f4a3a)" role="img" aria-label="Lakeside swing at dusk"></div>
  <div class="photo feed-photo" style="left:710px;background:linear-gradient(180deg,#9f8d83,#55534d 60%,#3c4a3e)" role="img" aria-label="Outdoor courtyard gathering by a brick building"></div>
  <div class="photo feed-photo" style="left:914px;background:linear-gradient(160deg,#c2a57d,#6f5a45)" role="img" aria-label="Woman relaxing in a white robe in a lounge"></div>
  <div class="btn btn-green" style="left:525px;top:3593px;width:150px;height:50px">Follow us</div>

  <!-- footer -->
  <svg class="abs" style="left:0;top:3730px" width="1200" height="469" viewBox="0 0 1200 469">
    <path d="M0 60 C300 20 650 15 985 50 C650 35 300 50 0 95 Z" fill="#1fa8d8"/>
    <path d="M300 62 C650 60 950 75 1200 105 L1200 135 C950 100 650 75 300 62 Z" fill="#78b800"/>
    <path d="M0 110 C350 60 800 70 1200 140 L1200 469 L0 469 Z" fill="#195a80"/>
  </svg>
  <div class="abs footer-brand"><span class="dot"></span>Mirvald</div>
  <div class="abs footer-col" style="left:513px">
    <h4>Links</h4>
    <ul><li>Home</li><li>About</li><li>Services</li><li>Fall Mini Retreat</li><li>Programs</li></ul>
  </div>
  <div class="abs footer-col" style="left:728px">
    <h4>Contact</h4>
    <ul><li>300 004 217</li><li>hello@mirvald.com</li></ul>
  </div>
  <div class="abs social" style="left:965px" aria-label="Social profile"></div>
  <div class="abs social" style="left:1027px" aria-label="Social profile"></div>
  <p class="abs copyright">Mirvald Health &amp; Wellness © 2024 &nbsp;All rights reserved. Privacy Policy</p>

</div>
</body>
</html>
```